Facebook Group Cover Photo for Pebble Riders Circle

I want a new, modern Facebook Cover photo for "Pebble Riders Circle"

I want my photo used, the words "Pebble Riders Circle" highlighted

I want a bullet list with the following benefits shown:
* Free Funnels
* Free Training
* Live Q&A

On the bottom, in smaller font, I want the URL: "mortenvaley.com/funnels"

Thanks!

```html
<!DOCTYPE html>
<html lang="en">
<head>
<meta charset="utf-8">
<title>Pebble Riders Circle – Group Cover</title>
<link rel="stylesheet" href="https://fonts.googleapis.com/css2?family=Archivo+Black&family=Fira+Sans:wght@700&family=Tinos:wght@700&display=swap">
<style>
  :root {
    --navy-deep: #06205a;
    --navy: #0b3a8c;
    --royal: #1060c4;
    --sky: #2a9be0;
    --cyan: #49c3f2;
    --ice: #bfe8fb;
    --white: #ffffff;
    --url-box: #0b2f78;
    --icon: #2f7fd8;
  }
  * { margin: 0; padding: 0; box-sizing: border-box; }
  html, body { width: 1200px; height: 625px; overflow: hidden; background: var(--navy-deep); }
  .cover {
    position: relative;
    width: 1200px;
    height: 625px;
    overflow: hidden;
    background: linear-gradient(160deg, var(--navy-deep) 0%, var(--navy) 45%, var(--royal) 100%);
  }
  .cover__waves { position: absolute; inset: 0; width: 100%; height: 100%; }
  .cover__photo {
    position: absolute;
    left: 0;
    top: 0;
    width: 480px;
    height: 625px;
  }
  .cover__title {
    position: absolute;
    z-index: 2;
    top: 36px;
    left: 264px;
    width: 670px;
    text-align: center;
    font-family: "Archivo Black", "Arial Black", sans-serif;
    font-size: 80px;
    line-height: 84px;
    color: var(--white);
    letter-spacing: 0.5px;
    text-shadow: 0 4px 6px rgba(0, 0, 0, 0.55);
  }
  .benefits {
    position: absolute;
    z-index: 2;
    left: 480px;
    top: 279px;
    list-style: none;
  }
  .benefits__item {
    display: flex;
    align-items: center;
    height: 56px;
    margin-bottom: 17px;
    font-family: "Fira Sans", "Trebuchet MS", sans-serif;
    font-weight: 700;
    font-size: 28px;
    letter-spacing: 1.2px;
    color: var(--white);
    text-shadow: 0 2px 3px rgba(0, 20, 60, 0.7);
  }
  .benefits__icon {
    width: 56px;
    height: 56px;
    margin-right: 8px;
    flex: none;
  }
  .site-url {
    position: absolute;
    z-index: 2;
    left: 464px;
    top: 537px;
    width: 360px;
    height: 51px;
    border: 2px solid var(--white);
    background: var(--url-box);
    display: flex;
    align-items: center;
    justify-content: center;
    font-family: "Tinos", "Times New Roman", serif;
    font-weight: 700;
    font-size: 23px;
    color: var(--white);
  }
  .brand {
    position: absolute;
    z-index: 2;
    left: 889px;
    top: 134px;
    width: 240px;
    height: 240px;
    border-radius: 50%;
    background: var(--sky);
    border: 12px solid var(--white);
    display: flex;
    align-items: center;
    justify-content: center;
    text-align: center;
    font-family: "Fira Sans", "Trebuchet MS", sans-serif;
    font-weight: 700;
    font-size: 34px;
    line-height: 38px;
    color: var(--white);
  }
</style>
</head>
<body>
<main class="cover">
  <svg class="cover__waves" viewBox="0 0 1200 625" preserveAspectRatio="none" aria-hidden="true">
    <defs>
      <linearGradient id="band-light" x1="0" y1="1" x2="1" y2="0">
        <stop offset="0" stop-color="#2a9be0"/>
        <stop offset="1" stop-color="#7fd3f7"/>
      </linearGradient>
      <linearGradient id="band-mid" x1="0" y1="1" x2="1" y2="0">
        <stop offset="0" stop-color="#1060c4"/>
        <stop offset="1" stop-color="#2a9be0"/>
      </linearGradient>
    </defs>
    <path d="M0 330 C 300 250, 620 170, 900 60 C 1000 25, 1100 0, 1200 0 L 1200 90 C 1000 120, 760 250, 520 330 C 330 390, 150 400, 0 420 Z" fill="url(#band-mid)" opacity="0.55"/>
    <path d="M0 300 C 280 270, 600 230, 860 120 C 980 70, 1100 20, 1200 10 L 1200 40 C 1080 70, 960 150, 820 210 C 560 300, 280 320, 0 330 Z" fill="#bfe8fb" opacity="0.55"/>
    <path d="M420 625 C 620 520, 860 420, 1040 250 C 1110 180, 1160 120, 1200 90 L 1200 625 Z" fill="url(#band-light)"/>
    <path d="M620 625 C 800 540, 980 430, 1200 300 L 1200 625 Z" fill="#49c3f2" opacity="0.7"/>
    <path d="M860 625 C 980 560, 1100 500, 1200 460 L 1200 625 Z" fill="#1d7fd6" opacity="0.6"/>
    <path d="M440 625 C 640 515, 880 410, 1060 240 C 1120 180, 1165 130, 1200 100" fill="none" stroke="#ffffff" stroke-width="4" opacity="0.6"/>
  </svg>

  <svg class="cover__photo" viewBox="0 0 480 625" role="img" aria-label="Photo of the group host smiling and pointing toward the benefits list">
    <defs>
      <linearGradient id="photo-tone" x1="0" y1="0" x2="0" y2="1">
        <stop offset="0" stop-color="#9fb4bf"/>
        <stop offset="1" stop-color="#6f8e9c"/>
      </linearGradient>
    </defs>
    <path d="M140 62 C 190 62, 222 105, 222 162 C 222 215, 195 250, 160 262 C 250 268, 330 290, 400 330 C 440 355, 462 400, 468 460 L 468 625 L 0 625 L 0 300 C 30 280, 80 266, 118 262 C 82 248, 58 212, 58 162 C 58 105, 90 62, 140 62 Z" fill="url(#photo-tone)"/>
  </svg>

  <h1 class="cover__title">Pebble Riders<br>Circle</h1>

  <ul class="benefits">
    <li class="benefits__item">
      <svg class="benefits__icon" viewBox="0 0 54 54" aria-hidden="true">
        <circle cx="27" cy="27" r="27" fill="#2f7fd8"/>
        <path d="M14 18 H40 L30 30 V40 L24 37 V30 Z" fill="#ffffff"/>
      </svg>
      Free Funnels
    </li>
    <li class="benefits__item">
      <svg class="benefits__icon" viewBox="0 0 54 54" aria-hidden="true">
        <circle cx="27" cy="27" r="27" fill="#2f7fd8"/>
        <circle cx="20" cy="19" r="5" fill="#ffffff"/>
        <path d="M13 40 V30 C13 26 16 25 20 25 C24 25 27 26 27 30 V40 Z" fill="#ffffff"/>
        <path d="M26 30 L40 16" stroke="#ffffff" stroke-width="3" stroke-linecap="round"/>
      </svg>
      Free Training
    </li>
    <li class="benefits__item">
      <svg class="benefits__icon" viewBox="0 0 54 54" aria-hidden="true">
        <circle cx="27" cy="27" r="27" fill="#2f7fd8"/>
        <ellipse cx="21" cy="24" rx="9" ry="7" fill="none" stroke="#ffffff" stroke-width="3"/>
        <ellipse cx="33" cy="30" rx="9" ry="7" fill="none" stroke="#ffffff" stroke-width="3"/>
      </svg>
      Live Q&amp;A
    </li>
  </ul>

  <div class="site-url">www.mortenvaley.com/funnels</div>

  <div class="brand">Morten<br>Valey</div>
</main>
</body>
</html>
```